Health insurance Facts Infographic

We need an infographic compiling the research in the attached report. Can cover all topics in the report, or a few. It needs to be easy for our readers to understand and should follow the design guide/ color scheme laid out in our website www.covernook.com and attached infographic

Requirements
Must have
• • An estimated 27.5 million people, 8.5% of the population, went without health insurance in 2018. That was an increase of 1.9 million uninsured people, or 0.5 percentage point.
In 2017, the number of people without health insurance increased to 28.0 million, up from 27.3 million the year before, according to the latest Civic Household Tally data released today.
• Working-age adults made up a much larger share of the uninsured population than any other age group. In fact, most uninsured people (84.6 percent) were 19- to 64-year-olds.
• The two largest groups in that age range are 26- to 34-year-olds and 35- to 44-year-olds. About 1 in 4 uninsured people were 26 to 34 years old, and about 1 in 5 people ages 34 to 44.
• Over half of all people without health insurance coverage were male (54.6 percent), even though the U.S. population has more women than men.
• About 4 in 10 uninsured people were non-Hispanic white, while nearly 6 in 10 people in the United States were non-Hispanic white.
• Other races and ethnic groups made up the majority of the uninsured population but less than half (39.3 percent) of the total population.
• The uninsured were disproportionately concentrated in the South.
Nice to have
• other supporting facts. Graphics maybe of people or bodies showing the statistics.

```html
<!DOCTYPE html>
<html lang="en">
<head>
<meta charset="utf-8">
<title>2018 Health Insurance Demographics</title>
<link rel="stylesheet" href="https://fonts.googleapis.com/css2?family=Montserrat:wght@400;600;700;800&family=Oswald:wght@300;400;500&family=Bebas+Neue&display=swap">
<style>
:root{
  --orange:#e8562c;
  --orange-dark:#b8361a;
  --red-deep:#9a2a12;
  --sky:#9be4fb;
  --sky-bright:#8fe0fb;
  --blue:#1ea5d6;
  --blue-light:#7fd8f5;
  --ink:#111111;
  --grey-bg:#f4f4f4;
  --white:#ffffff;
}
*{margin:0;padding:0;box-sizing:border-box}
html,body{width:1200px;height:3344px;overflow:hidden;background:var(--white)}
.canvas{position:relative;width:1200px;height:3344px;overflow:hidden;color:var(--ink);font-family:"Oswald",sans-serif}
.abs{position:absolute}
.header{left:0;top:0;width:1200px;height:138px}
.header-year{left:62px;top:10px;font-family:"Montserrat",sans-serif;font-weight:800;font-size:104px;color:var(--white);letter-spacing:1px;line-height:120px;white-space:nowrap}
.header-title{left:410px;top:0;width:760px;height:132px}
.brand{left:64px;top:168px;font-family:"Montserrat",sans-serif;font-weight:700;font-size:78px;color:var(--ink);letter-spacing:-2px;display:flex;align-items:center;gap:18px;white-space:nowrap}
.brand-dot{width:22px;height:22px;border-radius:50%;background:var(--ink)}
.hero-art{left:215px;top:175px;width:985px;height:535px;border-radius:260px 260px 40px 200px;background:radial-gradient(ellipse at 50% 55%,#f3f6f8 0%,#dfe9ef 60%,rgba(223,233,239,0) 100%)}
.umbrella-art{left:14px;top:760px;width:530px;height:500px;border-radius:40px;background:linear-gradient(160deg,#2b8fd0 0%,#5fb3e2 35%,#e5e7ea 70%,#d4d6d9 100%)}
.facts-title{left:565px;top:800px;font-family:"Montserrat",sans-serif;font-weight:700;font-size:40px;line-height:48px;white-space:nowrap}
.facts-years{left:565px;top:846px;font-family:"Montserrat",sans-serif;font-weight:800;font-size:74px;color:var(--sky-bright);line-height:90px;white-space:nowrap}
.timeline-line{left:717px;top:1084px;width:0;height:140px;border-left:3px dotted #888}
.year-tag{font-family:"Oswald",sans-serif;font-weight:500;font-size:25px;white-space:nowrap}
.fact-icon{width:128px;height:128px;border-radius:50%;background:var(--white);border:3px solid #d8d8d8;box-shadow:0 2px 6px rgba(0,0,0,.2);display:flex;align-items:center;justify-content:center}
.fact-icon span{display:block;width:106px;height:106px;border-radius:50%;background:var(--orange)}
.fact-text{left:815px;width:335px;font-family:"Oswald",sans-serif;font-weight:300;font-size:27px;line-height:31.5px;color:var(--ink)}
.lead{left:0;width:1200px;text-align:center;font-family:"Oswald",sans-serif;font-weight:500;font-size:33px;line-height:40px;white-space:nowrap}
.lead-figure{left:0;top:1663px;width:1200px;text-align:center;font-family:"Montserrat",sans-serif;font-weight:700;font-size:58px;line-height:70px;white-space:nowrap}
.age-ring{width:326px;height:326px;border-radius:50%;border:14px solid var(--orange);background:var(--white);display:flex;align-items:center;justify-content:center}
.age-ring span{display:block;width:210px;height:220px;border-radius:40px;background:linear-gradient(180deg,#cfd3db,#9aa0ac)}
.age-label{width:360px;text-align:center;font-family:"Oswald",sans-serif;font-weight:500;font-size:40px;line-height:48px;white-space:nowrap}
.to-label{left:578px;top:1925px;font-family:"Oswald",sans-serif;font-weight:500;font-size:37px}
.panel{top:2237px;height:350px}
.panel-left{left:0;width:598px;background:var(--sky)}
.panel-right{left:602px;width:598px;background:var(--orange)}
.panel-title{font-family:"Montserrat",sans-serif;font-weight:700;font-size:29px;line-height:36px;color:var(--ink);white-space:nowrap}
.tree{position:absolute;border-left:2px solid var(--white)}
.branch{position:absolute;height:2px;background:var(--white)}
.node{position:absolute;width:14px;height:14px;border-radius:50%;background:var(--white)}
.item{position:absolute;font-family:"Montserrat",sans-serif;font-weight:700;font-size:23px;line-height:29px;color:var(--ink);white-space:nowrap}
.split-shadow{left:0;top:2587px;width:1200px;height:14px;background:linear-gradient(180deg,rgba(0,0,0,.08),rgba(0,0,0,0))}
.chart-head{width:480px;text-align:center;font-family:"Oswald",sans-serif;font-weight:300;font-size:31px;line-height:40px}
.chart-caption{width:480px;text-align:center;font-family:"Oswald",sans-serif;font-weight:500;font-size:31px;line-height:39px}
.footer-notes{left:0;top:3138px;width:1200px;height:186px;background:var(--white)}
.note{position:absolute;left:40px;width:1120px;display:flex;gap:22px;font-family:"Montserrat",sans-serif;font-weight:400;font-size:24.5px;line-height:31px;color:var(--ink)}
.note svg{flex:0 0 40px}
.footer-bar{left:0;top:3324px;width:1200px;height:20px;background:var(--orange)}
</style>
</head>
<body>
<div class="canvas">

  <svg class="abs" style="left:0;top:0" width="1200" height="3344" aria-hidden="true">
    <rect x="0" y="135" width="1200" height="1500" fill="#f6f6f6"/>
    <polygon points="0,135 1200,135 1200,575 950,740 513,740 513,1030 0,1360" fill="var(--sky)"/>
    <rect x="513" y="740" width="687" height="470" fill="var(--white)"/>
    <polygon points="1200,575 1200,740 950,740" fill="var(--white)"/>
    <rect x="0" y="1635" width="1200" height="605" fill="#f6f6f6"/>
    <rect x="0" y="2587" width="1200" height="550" fill="#f7f7f7"/>
  </svg>

  <svg class="abs header" width="1200" height="138" aria-hidden="true">
    <polygon points="0,0 355,0 420,132 0,132" fill="var(--orange)"/>
    <rect x="0" y="132" width="1200" height="6" fill="var(--orange)"/>
  </svg>
  <div class="abs header-year">2018</div>
  <svg class="abs header-title" width="760" height="132" viewBox="0 0 760 132">
    <text x="2" y="98" textLength="752" lengthAdjust="spacingAndGlyphs" font-family="'Bebas Neue',sans-serif" font-size="82" fill="var(--orange)">HEALTH INSURANCE DEMOGRAPHICS</text>
  </svg>

  <div class="abs brand">covernook<span class="brand-dot"></span></div>
  <div class="abs hero-art" role="img" aria-label="Illustration of doctors and patients beneath a green umbrella beside a health insurance form, a shield and a wallet of banknotes"></div>

  <div class="abs umbrella-art" role="img" aria-label="Illustration of a family standing on an insurance policy document under a large blue umbrella with an orange heart and a pen"></div>

  <div class="abs facts-title">HEALTH INSURANCE FACTS</div>
  <div class="abs facts-years">2017 - 2018</div>

  <div class="abs timeline-line"></div>
  <div class="abs year-tag" style="left:556px;top:1004px">In 2018</div>
  <div class="abs fact-icon" style="left:654px;top:956px" role="img" aria-label="Insurance clipboard icon"><span></span></div>
  <div class="abs fact-text" style="top:966px">An estimated 27.5 million people, 8.5% of the population, went without health insurance. That was an increase of 1.9 million uninsured people, or 0.5 percentage point.</div>

  <div class="abs year-tag" style="left:556px;top:1272px">In 2017</div>
  <div class="abs fact-icon" style="left:654px;top:1222px" role="img" aria-label="Family under umbrella icon"><span></span></div>
  <div class="abs fact-text" style="top:1232px">The number of people without health insurance increased to 28.0 million, up from 27.3 million the year before, according to the latest Civic Household Tally data released today.</div>

  <div class="abs lead" style="top:1547px">Working-age adults made up a much larger share of the uninsured population</div>
  <div class="abs lead" style="top:1613px">than any other age group. In fact, most uninsured people</div>
  <div class="abs lead-figure">(84.6 percent) were</div>

  <div class="abs age-ring" style="left:181px;top:1772px" role="img" aria-label="Illustration of a young man and young woman"><span></span></div>
  <div class="abs age-ring" style="left:694px;top:1772px" role="img" aria-label="Illustration of two older men cheering with walking canes"><span></span></div>
  <svg class="abs" style="left:563px;top:1908px" width="80" height="24" aria-hidden="true">
    <line x1="2" y1="12" x2="70" y2="12" stroke="var(--ink)" stroke-width="3"/>
    <polygon points="78,12 64,4 64,20" fill="var(--ink)"/>
  </svg>
  <div class="abs to-label">To</div>
  <div class="abs age-label" style="left:164px;top:2112px">19 Years Old</div>
  <div class="abs age-label" style="left:677px;top:2112px">64 Years Old</div>

  <div class="abs panel panel-left">
    <div class="abs panel-title" style="left:70px;top:50px">THE TWO LARGEST GROUPS<br>IN THAT AGE RANGE ARE</div>
    <div class="tree" style="left:78px;top:136px;width:0;height:126px"></div>
    <div class="branch" style="left:78px;top:171px;width:112px"></div>
    <div class="node" style="left:183px;top:165px"></div>
    <div class="branch" style="left:78px;top:260px;width:112px"></div>
    <div class="node" style="left:183px;top:254px"></div>
    <div class="item" style="left:222px;top:157px">26- TO 34-YEAR-OLDS AND</div>
    <div class="item" style="left:222px;top:246px">35- TO 44-YEAR-OLDS</div>
  </div>
  <div class="abs panel panel-right">
    <div class="abs panel-title" style="left:60px;top:68px">ABOUT</div>
    <div class="tree" style="left:66px;top:136px;width:0;height:126px"></div>
    <div class="branch" style="left:66px;top:171px;width:112px"></div>
    <div class="node" style="left:171px;top:165px"></div>
    <div class="branch" style="left:66px;top:260px;width:112px"></div>
    <div class="node" style="left:171px;top:254px"></div>
    <div class="item" style="left:210px;top:157px">1 IN 4 UNINSURED PEOPLE<br>WERE 26 TO 34 YEARS OLD</div>
    <div class="item" style="left:210px;top:246px">1 IN 5 PEOPLE AGES 34 TO<br>44.</div>
  </div>
  <div class="abs split-shadow"></div>

  <div class="abs chart-head" style="left:67px;top:2628px">Over half of all people without health insurance coverage were male</div>
  <div class="abs chart-head" style="left:644px;top:2628px">Other races and ethnic groups made up the majority of the uninsured population</div>

  <svg class="abs" style="left:140px;top:2725px" width="340" height="290" role="img" aria-label="Ring chart: 54.6 percent of uninsured people were male">
    <g transform="translate(170,125) scale(1,0.62)">
      <circle cx="0" cy="75" r="128" fill="none" stroke="var(--red-deep)" stroke-width="64"/>
      <circle cx="0" cy="40" r="128" fill="none" stroke="var(--red-deep)" stroke-width="64"/>
      <circle cx="0" cy="0" r="128" fill="none" stroke="var(--orange)" stroke-width="64"/>
      <circle cx="0" cy="75" r="128" fill="none" stroke="var(--blue)" stroke-width="64" stroke-dasharray="250 554" stroke-dashoffset="-76"/>
      <circle cx="0" cy="40" r="128" fill="none" stroke="var(--blue)" stroke-width="64" stroke-dasharray="250 554" stroke-dashoffset="-76"/>
      <circle cx="0" cy="0" r="128" fill="none" stroke="var(--blue-light)" stroke-width="64" stroke-dasharray="250 554" stroke-dashoffset="-76"/>
    </g>
    <text x="122" y="245" font-family="Montserrat,sans-serif" font-weight="700" font-size="23" fill="#ffffff">54.6%</text>
  </svg>

  <svg class="abs" style="left:730px;top:2725px" width="340" height="290" role="img" aria-label="Ring chart: other races and ethnic groups were 39.3 percent of the total population">
    <g transform="translate(170,125) scale(1,0.62)">
      <circle cx="0" cy="75" r="128" fill="none" stroke="var(--red-deep)" stroke-width="64"/>
      <circle cx="0" cy="40" r="128" fill="none" stroke="var(--red-deep)" stroke-width="64"/>
      <circle cx="0" cy="0" r="128" fill="none" stroke="var(--orange)" stroke-width="64"/>
      <circle cx="0" cy="75" r="128" fill="none" stroke="var(--blue)" stroke-width="64" stroke-dasharray="210 594" stroke-dashoffset="-110"/>
      <circle cx="0" cy="40" r="128" fill="none" stroke="var(--blue)" stroke-width="64" stroke-dasharray="210 594" stroke-dashoffset="-110"/>
      <circle cx="0" cy="0" r="128" fill="none" stroke="var(--blue-light)" stroke-width="64" stroke-dasharray="210 594" stroke-dashoffset="-110"/>
    </g>
    <text x="88" y="255" font-family="Montserrat,sans-serif" font-weight="700" font-size="23" fill="#ffffff">39.3%</text>
  </svg>

  <div class="abs chart-caption" style="left:67px;top:3019px">Even though the U.S. population has more women than men.</div>
  <div class="abs chart-caption" style="left:644px;top:3019px">But less than half of the total population.</div>

  <div class="abs footer-notes">
    <div class="note" style="top:42px">
      <svg width="40" height="36" viewBox="0 0 40 36" aria-hidden="true"><polyline points="3,18 15,30 37,4" fill="none" stroke="var(--orange)" stroke-width="5" stroke-linecap="round" stroke-linejoin="round"/></svg>
      <p>About 4 in 10 uninsured people were non-Hispanic white, while nearly 6 in 10 people in the United States were non-Hispanic white.</p>
    </div>
    <div class="note" style="top:130px">
      <svg width="40" height="36" viewBox="0 0 40 36" aria-hidden="true"><polyline points="3,18 15,30 37,4" fill="none" stroke="var(--orange)" stroke-width="5" stroke-linecap="round" stroke-linejoin="round"/></svg>
      <p>The uninsured were disproportionately concentrated in the South.</p>
    </div>
  </div>
  <div class="abs footer-bar"></div>

</div>
</body>
</html>
```